Slatebook App Analytics Dashboard Design

Our app is designed for visitors centers and hotel/lodging concierges to assist (and allow) travelers to book tours and activities on-site with a kiosk or at front desk. This analytics dashboard will help the hotels or visitors centers owners and employees to understand the activity within their app for their specific business.

We would like this to be modern, clean and sleek and really stand out when we highlight it at an upcoming presentation/conference. The stats we would like to show are:
(By day/month/time period)
Number of Bookings
Source of Bookings i.e. website vs mobile vs kiosk (% of a whole)
Top 5 tour operators booked (and volume of each)
Top 5 tours booked (and volume of each)
Commissions earned (*admin only option - won't show for regular users)

I am including some screen shots of our current Slatebook app to see our general design and color palate. We would like to use this library: https://quillarch.com/open-source/meridian/gallery

This could lead to further UX design improvements for our current app and future projects. I will be paying out a winner and will provide feedback as the contest goes on.

Target Market(s)

Hotel Concierges & Managers, Visitor Bureau Managers and Employees

Industry/Entity Type

Travel Industry

Font styles to use
Other font styles liked:
• Apple Fonts: San Francisco

Requirements
Must have
• We would like to use this library: https://quillarch.com/open-source/meridian/gallery
• The stats we would like to show are:
• (By day/month/time period)
• Number of Bookings
• Source of Bookings i.e. website vs mobile vs kiosk (% of a whole)
• Top 5 tour operators booked (and volume of each)
• Top 5 tours booked (and volume of each)
• Commissions earned (*admin only option - won't show for regular users)
Nice to have
• Would be nice to have an easy way for users to toggle between time periods that are common and also choose dates from drop down calendars.
• Will be used on an Slatebook and Slatebook Max

```html
<!DOCTYPE html>
<html lang="en">
<head>
<meta charset="utf-8">
<title>Slatebook Analytics Dashboard</title>
<link rel="stylesheet" href="https://fonts.googleapis.com/css2?family=Roboto:wght@300;400;500&display=swap">
<style>
:root{
  --sky:#a9d4f5;
  --violet:#5f47a2;
  --panel:#f4f6f9;
  --card:#ffffff;
  --line:#e6eaef;
  --ink:#58636e;
  --ink-soft:#8d98a4;
  --ink-faint:#b9c3cd;
  --desktop:#5bc6e8;
  --mobile:#a6f0cc;
  --kiosk:#e690e0;
  --blue:#4fc3f3;
  --red:#ff6a5f;
  --yellow:#ffbf1f;
  --green:#4fe7a1;
  --slate:#4f5d6b;
  --bar-gold:#ffbb00;
  --bar-blue:#5bc4f7;
  --bar-violet:#5d46a3;
  --bar-mint:#5ceccb;
  --bar-pink:#ff5a9c;
}
*{margin:0;padding:0;box-sizing:border-box}
html,body{width:1200px;height:859px;overflow:hidden}
body{font-family:"Roboto",sans-serif;background:var(--sky);position:relative;color:var(--ink)}
.backdrop{position:absolute;inset:0}
.dashboard{position:absolute;left:142px;top:86px;width:915px;height:686px;background:var(--panel);box-shadow:0 10px 40px rgba(40,30,90,.35)}
.toolbar{height:46px;background:var(--card);position:relative;font-size:13px;font-weight:300;color:var(--ink-faint)}
.toolbar span{position:absolute;top:15px}
.toolbar .label{left:607px}
.toolbar .period{left:718px}
.section-title{position:absolute;font-size:13px;font-weight:400;color:var(--ink)}
.card{position:absolute;width:422px;height:259px;background:var(--card);border:1px solid var(--line);border-radius:3px}
.count{position:absolute;left:0;right:0;top:66px;text-align:center;font-size:82px;font-weight:400;color:#67737e;line-height:1}
.count-label{position:absolute;left:0;right:0;top:166px;text-align:center;font-size:16px;letter-spacing:2px;color:var(--ink-faint);font-weight:300}
.card svg{position:absolute;left:0;top:0}
.axis{font-size:7.5px;fill:#707b86;letter-spacing:.5px}
.legend{font-size:8px;fill:var(--ink-soft);letter-spacing:.5px}
.op-name{font-size:10.5px;fill:var(--ink-soft);letter-spacing:.6px}
.op-pct{font-size:16px;font-weight:500}
.tour-name{font-size:12px;fill:var(--ink);letter-spacing:.6px}
</style>
</head>
<body>
<svg class="backdrop" width="1200" height="859" aria-hidden="true">
  <polygon points="0,104 1200,572 1200,859 0,859" fill="var(--violet)"/>
</svg>

<main class="dashboard">
  <header class="toolbar">
    <span class="label">Arrange View by</span>
    <span class="period">By day/month/time period</span>
  </header>

  <h2 class="section-title" style="left:34px;top:66px">Number of Bookings</h2>
  <h2 class="section-title" style="left:482px;top:66px">Source of Bookings</h2>
  <h2 class="section-title" style="left:34px;top:375px">Top 5 Tour Operators Booked</h2>
  <h2 class="section-title" style="left:481px;top:375px">Top 5 Tours Booked</h2>

  <section class="card bookings-card" style="left:23px;top:94px">
    <div class="count">69</div>
    <div class="count-label">Bookings</div>
  </section>

  <section class="card source-card" style="left:470px;top:94px">
    <svg width="422" height="259" viewBox="0 0 422 259">
      <g class="legend">
        <circle cx="98" cy="23" r="4.5" fill="var(--desktop)"/><text x="111" y="26">DESKTOP</text>
        <circle cx="208" cy="23" r="4.5" fill="var(--mobile)"/><text x="220" y="26">MOBILE</text>
        <circle cx="309" cy="23" r="4.5" fill="var(--kiosk)"/><text x="322" y="26">KIOSK</text>
      </g>
      <g fill="#f8f9fb">
        <rect x="58" y="45" width="28" height="197"/><rect x="122" y="45" width="28" height="197"/>
        <rect x="184" y="45" width="28" height="197"/><rect x="244" y="45" width="28" height="197"/>
        <rect x="308" y="45" width="28" height="197"/><rect x="370" y="45" width="28" height="197"/>
      </g>
      <g class="axis">
        <text x="18" y="54">100%</text><text x="22" y="81">80%</text><text x="22" y="108">60%</text>
        <text x="22" y="135">40%</text><text x="22" y="161">30%</text><text x="22" y="188">20%</text>
        <text x="22" y="215">10%</text><text x="26" y="242">0%</text>
      </g>
      <polygon fill="var(--desktop)" fill-opacity=".85" points="84,242 90,150 122,107 146,123 188,98 200,119 220,125 240,157 264,143 274,111 304,98 324,155 366,139 384,129 398,146 398,242"/>
      <polygon fill="var(--mobile)" fill-opacity=".9" points="54,242 58,215 84,191 112,163 152,150 180,119 200,169 248,195 280,189 310,137 352,124 388,187 398,242"/>
      <polygon fill="var(--kiosk)" fill-opacity=".85" points="54,242 84,208 108,211 124,169 144,179 168,175 202,214 236,205 248,217 280,203 316,218 356,189 388,215 398,242"/>
    </svg>
  </section>

  <section class="card operators-card" style="left:23px;top:402px">
    <svg width="422" height="259" viewBox="0 0 422 259">
      <g fill="none" stroke-width="10">
        <circle cx="206" cy="130" r="72" stroke="var(--blue)" stroke-dasharray="70.4 382" transform="rotate(212 206 130)"/>
        <circle cx="206" cy="130" r="72" stroke="var(--blue)" stroke-dasharray="70.4 382" transform="rotate(-88 206 130)"/>
        <circle cx="206" cy="130" r="72" stroke="var(--red)" stroke-dasharray="70.4 382" transform="rotate(152 206 130)"/>
        <circle cx="206" cy="130" r="72" stroke="var(--yellow)" stroke-dasharray="70.4 382" transform="rotate(92 206 130)"/>
        <circle cx="206" cy="130" r="72" stroke="var(--green)" stroke-dasharray="70.4 382" transform="rotate(32 206 130)"/>
        <circle cx="206" cy="130" r="60" stroke="var(--blue)" stroke-dasharray="58.6 318" transform="rotate(212 206 130)"/>
        <circle cx="206" cy="130" r="60" stroke="var(--blue)" stroke-dasharray="58.6 318" transform="rotate(-88 206 130)"/>
        <circle cx="206" cy="130" r="60" stroke="var(--red)" stroke-dasharray="58.6 318" transform="rotate(152 206 130)"/>
        <circle cx="206" cy="130" r="60" stroke="var(--yellow)" stroke-dasharray="58.6 318" transform="rotate(92 206 130)"/>
        <circle cx="206" cy="130" r="60" stroke="var(--green)" stroke-dasharray="58.6 318" transform="rotate(32 206 130)"/>
      </g>
      <g fill="none" stroke="var(--slate)" stroke-width="6">
        <circle cx="206" cy="130" r="66" stroke-dasharray="57.6 400" transform="rotate(-25 206 130)"/>
        <circle cx="206" cy="130" r="76" stroke-dasharray="66.3 420" transform="rotate(-25 206 130)"/>
        <circle cx="206" cy="130" r="86" stroke-dasharray="75.1 470" transform="rotate(-25 206 130)"/>
      </g>
      <text class="op-name" x="78" y="31">Aldergate Tours</text>
      <text class="op-pct" x="91" y="62" fill="var(--blue)">40%</text>
      <text class="op-name" x="38" y="105">Hazel’s Tour</text>
      <text class="op-pct" x="52" y="138" fill="var(--red)">20%</text>
      <text class="op-name" x="59" y="198">Kestrel Ltd</text>
      <text class="op-pct" x="71" y="229" fill="var(--yellow)">17%</text>
      <text class="op-name" x="332" y="80">Wayfarer</text>
      <text class="op-pct" x="342" y="110" fill="var(--slate)">9%</text>
      <text class="op-name" x="264" y="208">Brightfield Tours</text>
      <text class="op-pct" x="294" y="237" fill="var(--green)">12%</text>
    </svg>
  </section>

  <section class="card tours-card" style="left:470px;top:402px">
    <svg width="422" height="259" viewBox="0 0 422 259">
      <rect x="19" y="55" width="176" height="26" fill="var(--bar-gold)"/>
      <rect x="19" y="85" width="140" height="25" fill="var(--bar-blue)"/>
      <rect x="19" y="113" width="137" height="25" fill="var(--bar-violet)"/>
      <rect x="19" y="141" width="126" height="24" fill="var(--bar-mint)"/>
      <rect x="19" y="169" width="57" height="24" fill="var(--bar-pink)"/>
      <g class="tour-name" text-anchor="end">
        <text x="388" y="73">Portland Brewery Tour</text>
        <text x="388" y="104">Music Crawl</text>
        <text x="388" y="133">Art &amp; Architecture</text>
        <text x="388" y="160">Sip 52 Tour</text>
        <text x="388" y="186">Walking Tour</text>
      </g>
    </svg>
  </section>
</main>
</body>
</html>
```